Flyer Design Project

We need a flyer design for a 1 year old domestic cleaning company based in Wiltshire, England. We provide households with high quality, hard working cleaners. We would like to see designs which use blue (the colour on the logo attatched). The final design should communicate a clean, premier and thorough service in a clear and bold way. We would like the flyer to be A5 with a single sided design. We have attached an A5 word document with the words we would like to be used in the design, what we need is for you to give it some life, colour, artwork and a professional touch. We are perfectionsists which we would like to illustrate to our customer through this flyer.
Updates

payment has been guaranteed!

Sorry..... please no pictures of females on the designs. many thanks

Target Market(s)

females with higher than average income, aged 30-50. Have families and work 9-5.

Industry/Entity Type

It Company

Requirements
Must have
• The flyer must include the logo attatched and the words in the A5 document attatched. With RELIABLE CLEANERS preferably the headline. A5 - single sided.
The Flyer must also include our introductory offer.....
First Clean FREE
Allow us to demonstrate our standards

this should be emphasised.

PLEASE NOTE: can this be added to the list of words on the flyer please:

Ironing service - one day turn around
Nice to have
• some pictures - nothing cheesey. Again, pictures should communicate our modern professional approach.

```html
<!DOCTYPE html>
<html lang="en">
<head>
<meta charset="utf-8">
<title>Brookmere Cleaners – Reliable Cleaners Flyer</title>
<link rel="stylesheet" href="https://fonts.googleapis.com/css2?family=Arvo:wght@400;700&family=Tinos:wght@400;700&display=swap">
<style>
  :root {
    --paper: #ffffff;
    --carpet: #d94a4c;
    --carpet-deep: #c63a3d;
    --photo-dark: #2f2f31;
    --photo-mid: #3e3e41;
    --headline-red: #e2212a;
    --headline-blue: #1f3f95;
    --ink: #1a1a1a;
    --brand-blue: #1f57a6;
    --stripe-top: #f2b9b9;
    --stripe-bottom: #ffffff;
  }
  * { margin: 0; padding: 0; box-sizing: border-box; }
  html, body {
    width: 864px; height: 1200px; overflow: hidden;
    background: var(--paper);
  }
  .flyer {
    position: relative;
    width: 864px; height: 1200px;
    background: var(--paper);
  }
  .carpet {
    position: absolute;
    left: 28px; top: 28px; width: 808px; height: 1140px;
    background: radial-gradient(ellipse at 50% 40%, var(--carpet) 0%, var(--carpet-deep) 100%);
  }
  .vacuum-photo {
    position: absolute;
    left: 210px; top: 28px; width: 440px; height: 384px;
    background: linear-gradient(180deg, var(--photo-mid) 0%, var(--photo-dark) 100%);
  }
  .clean-stripe {
    position: absolute;
    left: 215px; top: 412px; width: 433px; height: 756px;
    background: linear-gradient(180deg, var(--stripe-top) 0%, var(--stripe-bottom) 55%, var(--stripe-bottom) 100%);
  }
  .copy {
    position: absolute;
    left: 215px; top: 0; width: 433px; height: 1200px;
    text-align: center;
  }
  .copy > * { position: absolute; left: 0; width: 100%; }
  .headline {
    font-family: "Arvo", serif; font-weight: 400;
    line-height: 1; letter-spacing: -1px;
  }
  .headline--reliable { top: 436px; font-size: 72px; color: var(--headline-red); }
  .headline--cleaners { top: 510px; font-size: 62px; color: var(--headline-blue); }
  .offer {
    top: 576px;
    font-family: "Arvo", serif; font-size: 60px; line-height: 56px;
    color: var(--ink);
  }
  .offer-note {
    top: 742px;
    font-family: "Tinos", serif; font-size: 26px; line-height: 26px;
    color: var(--ink);
  }
  .services {
    top: 801px;
    list-style: none;
    font-family: "Tinos", serif; font-size: 24px; line-height: 26px;
    color: var(--ink);
  }
  .brand {
    top: 991px; height: 38px;
    display: flex; align-items: center; justify-content: center; gap: 10px;
  }
  .brand-mark {
    width: 34px; height: 34px; background: var(--brand-blue);
  }
  .brand-name {
    font-family: "Tinos", serif; font-weight: 700; font-size: 28px;
    color: var(--brand-blue);
  }
  .brand-tagline {
    top: 1044px;
    font-family: "Tinos", serif; font-weight: 700; font-size: 17px; line-height: 20px;
    color: var(--ink);
  }
  .phone {
    top: 1079px;
    font-family: "Tinos", serif; font-size: 44px; line-height: 50px;
    color: var(--headline-red);
  }
  .email {
    top: 1128px;
    font-family: "Tinos", serif; font-size: 20px; line-height: 24px;
    color: var(--ink);
  }
</style>
</head>
<body>
<main class="flyer">
  <div class="carpet" role="img" aria-label="Close-up photograph of red carpet texture"></div>
  <div class="clean-stripe"></div>
  <div class="vacuum-photo" role="img" aria-label="Photograph of a black vacuum cleaner head on the carpet"></div>

  <section class="copy">
    <h1 class="headline headline--reliable">RELIABLE</h1>
    <h2 class="headline headline--cleaners">CLEANERS!</h2>
    <p class="offer">FIRST<br>CLEAN<br>FREE</p>
    <p class="offer-note">Allow us to demonstrate<br>our standards</p>
    <ul class="services">
      <li>Personalised service</li>
      <li>• Constantly thorough</li>
      <li>• Hassel free • Insured</li>
      <li>• Regular weekly cleans</li>
      <li>• No contracts</li>
      <li>Ironing service - one day turn around</li>
    </ul>
    <div class="brand">
      <span class="brand-mark"></span>
      <span class="brand-name">Brookmere Cleaners</span>
    </div>
    <p class="brand-tagline">Premier Domestic Cleaners</p>
    <p class="phone">Tele: 07700900123</p>
    <p class="email">Email: hello@brookmerecleaners.co.uk</p>
  </section>
</main>
</body>
</html>
```